Book cover entitled #GLOWBEYONDIT

Design front book cover (self-self-portait photos included) for my first book entitled -

#GLOWBEYONDIT (may be best to have different shades of colour for glow beyond it to stand off you). I'm intentionally choosing a title that is essentially a hashtag.

Subtitle - Rewriting quiet inner battles

Concept of cover - left side of my face is shaded with shame and right side is brighter and hopeful. I have also include my logo.

Link for photos
https://www.filqorvex.com/sh/tq7mxd2kw9pl41a/BBR8NpXwQ3hLm6TzvKe2YUJ5b?dl=0

Target Market(s)

People (or friends & family) suffering with the shame of mental health struggles

Industry/Entity Type

Mental Health

Font styles to use
Other font styles liked:
• Avenir

Colors
3276b5
85acd3
cfdeed

Requirements
Must have
• Relatable, contemporary, authentic & compelling
• Link for photos
• https://www.filqorvex.com/sh/tq7mxd2kw9pl41a/BBR8NpXwQ3hLm6TzvKe2YUJ5b?dl=0
Nice to have
• Abstract & creative
Should not have
• Cheesy, plastic, pedestrian etc

```html
<!DOCTYPE html>
<html lang="en">
<head>
<meta charset="utf-8">
<title>#GLOWBEYONDIT — Book Cover Presentation</title>
<link rel="stylesheet" href="https://fonts.googleapis.com/css2?family=Nunito+Sans:wght@500;600;700&display=swap">
<style>
  :root {
    --page-bg: #ffffff;
    --cover-bg: #06080d;
    --spine-bg: #0b0d12;
    --photo-deep: #0a1226;
    --photo-mid: #1d3a78;
    --photo-light: #3276b5;
    --photo-glow: #cfdeed;
    --photo-soft: #85acd3;
    --accent-red: #ef2a2d;
    --title-white: #ffffff;
    --brand-blue: #85acd3;
    --brand-text: #b9c9dc;
  }
  * { margin: 0; padding: 0; box-sizing: border-box; }
  html, body {
    width: 1200px;
    height: 900px;
    overflow: hidden;
    background: var(--page-bg);
    font-family: "Nunito Sans", "Avenir", sans-serif;
  }
  .canvas {
    position: relative;
    width: 1200px;
    height: 900px;
  }

  /* Flat spine + front panel */
  .book-flat {
    position: absolute;
    left: 14px;
    top: 108px;
    width: 546px;
    height: 684px;
    display: flex;
  }
  .book-spine {
    position: relative;
    width: 62px;
    height: 684px;
    background: var(--spine-bg);
  }
  .spine-title {
    position: absolute;
    left: 50%;
    top: 70px;
    transform: translateX(-50%);
    writing-mode: vertical-rl;
    font-weight: 600;
    font-size: 34px;
    letter-spacing: 1px;
    text-transform: uppercase;
    color: var(--title-white);
    white-space: nowrap;
  }
  .spine-title .title-accent { color: var(--accent-red); }
  .spine-brand {
    position: absolute;
    left: 0;
    right: 0;
    bottom: 26px;
    display: flex;
    flex-direction: column;
    align-items: center;
    gap: 6px;
  }
  .spine-brand .brand-square {
    width: 26px;
    height: 26px;
    background: var(--brand-blue);
  }
  .spine-brand .brand-name {
    font-weight: 600;
    font-size: 10px;
    color: var(--brand-text);
    white-space: nowrap;
  }
  .book-front {
    position: relative;
    width: 484px;
    height: 684px;
    overflow: hidden;
  }
  .book-front .book-cover {
    transform: scale(0.76);
    transform-origin: top left;
  }

  /* Cover artwork (637 × 900 units) */
  .book-cover {
    position: absolute;
    left: 0;
    top: 0;
    width: 637px;
    height: 900px;
    background: var(--cover-bg);
    overflow: hidden;
  }
  .cover-large {
    left: 563px;
    top: 0;
  }
  .portrait-photo {
    position: absolute;
    inset: 0;
    background:
      radial-gradient(ellipse 17% 13% at 72% 38%, rgba(207,222,237,0.85) 0%, rgba(133,172,211,0.45) 55%, rgba(133,172,211,0) 100%),
      radial-gradient(ellipse 17% 10% at 70% 24%, rgba(133,172,211,0.55) 0%, rgba(50,118,181,0) 100%),
      radial-gradient(ellipse 45% 40% at 72% 72%, rgba(50,118,181,0.55) 0%, rgba(29,58,120,0.45) 45%, rgba(10,18,38,0) 100%),
      radial-gradient(ellipse 14% 18% at 96% 24%, rgba(133,172,211,0.25) 0%, rgba(133,172,211,0) 100%),
      radial-gradient(ellipse 70% 60% at 70% 60%, var(--photo-deep) 0%, rgba(10,18,38,0) 100%);
  }
  .cover-title {
    position: absolute;
    left: 35px;
    top: 40px;
    font-weight: 500;
    font-size: 135px;
    line-height: 126px;
    letter-spacing: 0;
    text-transform: uppercase;
    color: var(--title-white);
  }
  .cover-title .title-line { display: block; }
  .cover-title .title-accent { color: var(--accent-red); }
  .cover-subtitle {
    position: absolute;
    left: 63px;
    top: 470px;
    font-weight: 600;
    font-size: 30px;
    line-height: 32px;
    letter-spacing: 1px;
    text-transform: uppercase;
    color: var(--title-white);
  }
  .cover-subtitle .subtitle-line { display: block; }
  .cover-subtitle .subtitle-accent { color: var(--accent-red); }
  .author-brand {
    position: absolute;
    left: 70px;
    top: 758px;
    width: 110px;
    display: flex;
    flex-direction: column;
    align-items: center;
    gap: 10px;
  }
  .author-brand .brand-square {
    width: 44px;
    height: 44px;
    background: var(--brand-blue);
  }
  .author-brand .brand-name {
    font-weight: 600;
    font-size: 17px;
    color: var(--brand-text);
    white-space: nowrap;
  }
</style>
</head>
<body>
  <main class="canvas">

    <section class="book-flat" aria-label="Book spine and front cover">
      <div class="book-spine">
        <p class="spine-title">#Glow <span class="title-accent">Beyond</span> It</p>
        <div class="spine-brand">
          <span class="brand-square"></span>
          <span class="brand-name">lena hartwell</span>
        </div>
      </div>
      <div class="book-front">
        <div class="book-cover">
          <div class="portrait-photo" role="img" aria-label="Author self-portrait in a blue-toned shirt, face half in shadow and half lit, seated against a dark background"></div>
          <h2 class="cover-title">
            <span class="title-line">#Glow</span>
            <span class="title-line title-accent">Beyond</span>
            <span class="title-line">It</span>
          </h2>
          <p class="cover-subtitle">
            <span class="subtitle-line subtitle-accent">Rewriting</span>
            <span class="subtitle-line">Quiet</span>
            <span class="subtitle-line">Inner</span>
            <span class="subtitle-line">Battles</span>
          </p>
          <div class="author-brand">
            <span class="brand-square"></span>
            <span class="brand-name">lena hartwell</span>
          </div>
        </div>
      </div>
    </section>

    <section class="book-cover cover-large" aria-label="Front cover">
      <div class="portrait-photo" role="img" aria-label="Author self-portrait in a blue-toned shirt, face half in shadow and half lit, seated against a dark background"></div>
      <h1 class="cover-title">
        <span class="title-line">#Glow</span>
        <span class="title-line title-accent">Beyond</span>
        <span class="title-line">It</span>
      </h1>
      <p class="cover-subtitle">
        <span class="subtitle-line subtitle-accent">Rewriting</span>
        <span class="subtitle-line">Quiet</span>
        <span class="subtitle-line">Inner</span>
        <span class="subtitle-line">Battles</span>
      </p>
      <div class="author-brand">
        <span class="brand-square"></span>
        <span class="brand-name">lena hartwell</span>
      </div>
    </section>

  </main>
</body>
</html>
```